Medical VIP club - small design

Please read the specs in a design brief attached. Also we don't have logo in a Vector format and attaching the only version we have.

Industry/Entity Type

Club

```html
<!DOCTYPE html>
<html lang="en">
<head>
<meta charset="utf-8">
<title>Curavita – Medical VIP Club</title>
<link rel="stylesheet" href="https://fonts.googleapis.com/css2?family=Arimo:wght@400;700&family=Open+Sans:wght@600;700&display=swap">
<style>
  :root {
    --navy-deep: #15245a;
    --navy: #1f3373;
    --navy-mid: #29418a;
    --tab-top: #3f8cff;
    --tab-bottom: #0b46d8;
    --tab-active-top: #2b5ce6;
    --tab-active-bottom: #0a25a8;
    --band-light: #a9c4ff;
    --brand-blue: #2f86e6;
    --white: #ffffff;
    --ink-navy: #0b2447;
    --hero-violet: #8a56d6;
    --hero-indigo: #3a2a9a;
    --hero-lilac: #d6a6f0;
  }
  * { box-sizing: border-box; margin: 0; padding: 0; }
  html, body { width: 1200px; height: 1046px; overflow: hidden; }
  body {
    position: relative;
    font-family: "Arimo", Arial, sans-serif;
    background: linear-gradient(180deg, var(--navy-mid) 0%, var(--navy) 45%, var(--navy-deep) 100%);
    color: var(--white);
  }

  .site-header {
    position: absolute; left: 0; top: 0; width: 1200px; height: 279px;
    background: linear-gradient(180deg, #2a3f86 0%, #223777 60%, #1d306c 100%);
  }
  .header-band {
    position: absolute; left: 0; top: 241px; width: 1200px; height: 38px;
    background: linear-gradient(180deg, #c8d8ff 0%, var(--band-light) 100%);
  }
  .brand {
    position: absolute; left: 44px; top: 78px;
    display: flex; align-items: center; gap: 12px;
    font-family: "Arimo", Arial, sans-serif; font-weight: 700;
    font-size: 54px; color: var(--brand-blue); letter-spacing: -1px;
  }
  .brand-dot { width: 40px; height: 40px; border-radius: 50%; background: var(--brand-blue); }

  .hotline {
    position: absolute; left: 790px; top: 51px;
    display: flex; align-items: center; gap: 22px;
  }
  .hotline-icon {
    width: 104px; height: 104px; border-radius: 50%;
    background: radial-gradient(circle at 40% 30%, #6fa6ff 0%, #1d5ad6 55%, #0c2f8a 100%);
    box-shadow: 0 0 0 3px rgba(255,255,255,0.25), 0 4px 10px rgba(0,0,0,0.4);
    display: flex; align-items: center; justify-content: center;
  }
  .hotline-number {
    font-family: "Arimo", Arial, sans-serif; font-weight: 700;
    font-size: 47px; color: var(--white); letter-spacing: -0.5px;
    text-shadow: 2px 2px 0 #0d1c4a, -1px -1px 0 #0d1c4a, 1px -1px 0 #0d1c4a, -1px 1px 0 #0d1c4a;
  }

  .main-nav { position: absolute; left: 24px; top: 206px; display: flex; gap: 4px; }
  .nav-tab {
    width: 190px; height: 72px; border-radius: 14px 14px 0 0;
    background: linear-gradient(180deg, var(--tab-top) 0%, #1f66f0 50%, var(--tab-bottom) 100%);
    display: flex; align-items: center; justify-content: center;
    padding-top: 10px;
    font-size: 20px; color: var(--white); text-decoration: none;
    border-bottom: 4px solid #1448c8;
  }
  .nav-tab.is-active {
    background: linear-gradient(180deg, var(--tab-active-top) 0%, #1a3fcf 50%, var(--tab-active-bottom) 100%);
    border-bottom-color: #0b1f8a;
  }

  .hero {
    position: absolute; left: 24px; top: 290px; width: 1158px; height: 420px;
    border: 1px solid #8fa6e6; overflow: hidden;
  }
  .hero-photo {
    position: absolute; inset: 0;
    background:
      radial-gradient(ellipse at 50% 20%, var(--hero-lilac) 0%, transparent 55%),
      linear-gradient(90deg, var(--hero-violet) 0%, var(--hero-indigo) 30%, #4a36b0 50%, var(--hero-indigo) 70%, var(--hero-violet) 100%);
  }
  .hero-arrow { position: absolute; top: 186px; }
  .hero-arrow.prev { left: 10px; }
  .hero-arrow.next { right: 10px; }
  .hero-caption { position: absolute; left: 678px; top: 222px; width: 420px; }
  .hero-title {
    font-family: "Open Sans", Arial, sans-serif; font-weight: 600;
    font-size: 90px; line-height: 1; color: var(--ink-navy); letter-spacing: -2px;
    text-shadow: 0 0 6px rgba(255,255,255,0.9), 0 0 2px #fff;
  }
  .hero-text {
    margin: 10px 0 0 27px; font-weight: 700; font-size: 20px; line-height: 27px; color: var(--white);
  }

  .feature-row { position: absolute; left: 24px; top: 719px; display: flex; gap: 11px; }
  .feature-tile { width: 223px; height: 204px; border: 1px solid #cfd8f0; }
  .tile-hospital { background: linear-gradient(135deg, #2f7fd6 0%, #9cc7ef 60%, #e3eef8 100%); }
  .tile-travel { background: linear-gradient(135deg, #0f4fd0 0%, #2f86f0 60%, #7fbaff 100%); }
  .tile-resort { background: linear-gradient(180deg, #5aa8e8 0%, #e8f2f6 55%, #8f8a7c 100%); }
  .tile-doctors { background: linear-gradient(180deg, #f4f6f8 0%, #e4e9ee 100%); }
  .tile-membership { background: linear-gradient(135deg, #e9eef4 0%, #c6d2df 100%); }

  .site-footer {
    position: absolute; left: 0; top: 953px; width: 1200px; height: 93px;
    border-top: 2px solid #3b55a6;
    background: linear-gradient(180deg, #24397c 0%, #1b2d66 100%);
  }
  .social-links { position: absolute; left: 24px; top: 30px; display: flex; gap: 6px; }
  .social-square { width: 37px; height: 37px; border-radius: 4px; }
  .social-square.one { background: #3b5a9a; }
  .social-square.two { background: #3fb3e6; }
  .social-square.three { background: #f08a1c; }
  .copyright {
    position: absolute; left: 0; width: 1200px; top: 47px; text-align: center;
    font-size: 13px; color: var(--white);
  }
  .footer-brand {
    position: absolute; right: 22px; top: 26px;
    display: flex; align-items: center; gap: 8px;
    font-weight: 700; font-size: 34px; color: var(--brand-blue);
  }
  .footer-brand .brand-dot { width: 26px; height: 26px; }
</style>
</head>
<body>
  <header class="site-header">
    <div class="header-band"></div>
    <div class="brand"><span class="brand-dot"></span>Curavita</div>
    <div class="hotline">
      <div class="hotline-icon">
        <svg width="62" height="52" viewBox="0 0 62 52" aria-hidden="true">
          <path d="M4 16 C4 6 58 6 58 16 L58 22 L44 22 L44 15 L18 15 L18 22 L4 22 Z" fill="#fff"/>
          <path d="M16 24 L46 24 L54 46 L8 46 Z" fill="#fff"/>
          <circle cx="31" cy="35" r="7" fill="#1d5ad6"/>
          <circle cx="31" cy="35" r="3" fill="#fff"/>
        </svg>
      </div>
      <div class="hotline-number">416-555-010</div>
    </div>
    <nav class="main-nav">
      <a class="nav-tab" href="#">About Us</a>
      <a class="nav-tab" href="#">VIP Club</a>
      <a class="nav-tab" href="#">Services</a>
      <a class="nav-tab" href="#">Packages &amp; Prices</a>
      <a class="nav-tab is-active" href="#">Registration</a>
      <a class="nav-tab" href="#">Contacts</a>
    </nav>
  </header>

  <section class="hero">
    <div class="hero-photo" role="img" aria-label="Lavish palace hall with chandeliers and a draped throne, tinted violet"></div>
    <svg class="hero-arrow prev" width="60" height="68" viewBox="0 0 60 68" aria-hidden="true">
      <path d="M44 4 L14 34 L44 64" fill="none" stroke="rgba(200,210,235,0.8)" stroke-width="14"/>
    </svg>
    <svg class="hero-arrow next" width="60" height="68" viewBox="0 0 60 68" aria-hidden="true">
      <path d="M16 4 L46 34 L16 64" fill="none" stroke="rgba(200,210,235,0.8)" stroke-width="14"/>
    </svg>
    <div class="hero-caption">
      <h1 class="hero-title">VIP Club</h1>
      <p class="hero-text">Lorem ipsum dolor. Lorem ipsum dolor. Lorem ipsum dolor...</p>
    </div>
  </section>

  <section class="feature-row">
    <div class="feature-tile tile-hospital" role="img" aria-label="Hospital building with emergency sign"></div>
    <div class="feature-tile tile-travel" role="img" aria-label="Airplanes flying over a world map"></div>
    <div class="feature-tile tile-resort" role="img" aria-label="Couple on a seaside resort balcony"></div>
    <div class="feature-tile tile-doctors" role="img" aria-label="Team of doctors in white coats"></div>
    <div class="feature-tile tile-membership" role="img" aria-label="Pen resting on a membership terms document"></div>
  </section>

  <footer class="site-footer">
    <div class="social-links">
      <span class="social-square one"></span>
      <span class="social-square two"></span>
      <span class="social-square three"></span>
    </div>
    <p class="copyright">Copyright ©2010 Curavita. All Rights Reserved</p>
    <div class="footer-brand"><span class="brand-dot"></span>Curavita</div>
  </footer>
</body>
</html>
```